Packaging Design for a wafer product

Dorvenn is a leading chocolate manufacturer in Zimbabwe. Dorvenn is lauching a wafer product with layers of delicious Dorvenn chocolate in between. The product will be called Mokarund. The pack will be a six colour design printed on metallised polypropelene. We attach a photo of the product as well as photos of the existing chocolate portfolio to guide the designers. The design must be bright and appealing

Manufacturer

```html
<!DOCTYPE html>
<html lang="en">
<head>
<meta charset="utf-8">
<title>Mokarund wafer pack</title>
<link rel="stylesheet" href="https://fonts.googleapis.com/css2?family=Oswald:wght@500;600;700&display=swap">
<style>
  :root {
    --page: #ffffff;
    --crimp: #8b5a2b;
    --crimp-light: #a8743f;
    --crimp-dark: #6f4520;
    --body-dark: #5e3d22;
    --body-mid: #7b5533;
    --body-light: #b48a60;
    --swoosh: #dca36a;
    --purple: #55288a;
    --purple-light: #7a4bb0;
    --cream: #f4eee6;
    --ink: #3a2414;
    --white: #ffffff;
    --wafer-dark: #4a2a17;
    --wafer-light: #8a5a3a;
  }
  html, body {
    margin: 0;
    padding: 0;
    overflow: hidden;
    background: var(--page);
  }
  .canvas {
    position: relative;
    width: 1200px;
    height: 513px;
    overflow: hidden;
    background: var(--page);
    font-family: "Oswald", "Arial Narrow", sans-serif;
  }
  .pack-art {
    position: absolute;
    inset: 0;
    width: 1200px;
    height: 513px;
  }
  .brand-badge {
    position: absolute;
    left: 158px;
    top: 122px;
    width: 98px;
    height: 98px;
    border-radius: 50%;
    background: var(--cream);
    display: flex;
    align-items: center;
    justify-content: center;
    color: var(--ink);
    font-size: 23px;
    font-weight: 500;
  }
  .flavour-ribbon {
    position: absolute;
    left: 500px;
    top: 96px;
    width: 158px;
    height: 44px;
    display: flex;
    align-items: center;
    justify-content: center;
    color: var(--ink);
    font-size: 27px;
    font-weight: 600;
    font-style: italic;
  }
  .product-name {
    position: absolute;
    left: 406px;
    top: 168px;
    margin: 0;
    color: var(--white);
    font-size: 90px;
    font-weight: 600;
    line-height: 1;
    letter-spacing: 0;
  }
  .tagline {
    position: absolute;
    left: 442px;
    top: 274px;
    margin: 0;
    color: var(--white);
    font-size: 33px;
    font-weight: 500;
    line-height: 1;
  }
</style>
</head>
<body>
<div class="canvas">
  <svg class="pack-art" viewBox="0 0 1200 513" xmlns="http://www.w3.org/2000/svg">
    <defs>
      <linearGradient id="bodyShade" x1="0" y1="0" x2="1" y2="0">
        <stop offset="0" stop-color="var(--body-light)"/>
        <stop offset="0.25" stop-color="var(--body-mid)"/>
        <stop offset="0.7" stop-color="var(--body-dark)"/>
        <stop offset="1" stop-color="var(--body-mid)"/>
      </linearGradient>
      <linearGradient id="swooshShade" x1="0" y1="0" x2="1" y2="0">
        <stop offset="0" stop-color="var(--swoosh)" stop-opacity="0.6"/>
        <stop offset="0.45" stop-color="var(--swoosh)"/>
        <stop offset="1" stop-color="var(--swoosh)" stop-opacity="0.75"/>
      </linearGradient>
      <linearGradient id="waferShade" x1="0" y1="0" x2="1" y2="1">
        <stop offset="0" stop-color="var(--wafer-light)"/>
        <stop offset="1" stop-color="var(--wafer-dark)"/>
      </linearGradient>
      <pattern id="crimpLeft" width="10" height="16" patternUnits="userSpaceOnUse">
        <path d="M0 0 L10 8 L0 16 Z" fill="var(--page)"/>
      </pattern>
      <pattern id="crimpRight" width="10" height="16" patternUnits="userSpaceOnUse">
        <path d="M10 0 L0 8 L10 16 Z" fill="var(--page)"/>
      </pattern>
      <clipPath id="leftEnd"><polygon points="40,14 124,64 124,432 40,494"/></clipPath>
      <clipPath id="rightEnd"><polygon points="1160,14 1078,64 1078,432 1160,494"/></clipPath>
      <clipPath id="packBody"><rect x="114" y="66" width="974" height="364" rx="18"/></clipPath>
    </defs>

    <!-- crimped ends -->
    <g class="crimp-end" clip-path="url(#leftEnd)">
      <rect x="30" y="0" width="100" height="513" fill="var(--crimp)"/>
      <rect x="60" y="0" width="8" height="513" fill="var(--crimp-light)"/>
      <rect x="98" y="0" width="12" height="513" fill="var(--crimp-light)"/>
      <rect x="116" y="0" width="8" height="513" fill="var(--crimp-dark)"/>
    </g>
    <rect x="34" y="0" width="10" height="513" fill="url(#crimpLeft)"/>

    <g class="crimp-end" clip-path="url(#rightEnd)">
      <rect x="1070" y="0" width="100" height="513" fill="var(--crimp)"/>
      <rect x="1132" y="0" width="8" height="513" fill="var(--crimp-light)"/>
      <rect x="1092" y="0" width="12" height="513" fill="var(--crimp-light)"/>
      <rect x="1078" y="0" width="8" height="513" fill="var(--crimp-dark)"/>
    </g>
    <rect x="1156" y="0" width="10" height="513" fill="url(#crimpRight)"/>

    <!-- pack body -->
    <g class="pack-body" clip-path="url(#packBody)">
      <rect x="114" y="66" width="974" height="364" fill="url(#bodyShade)"/>
      <path class="swoosh" d="M114 110 C 300 150, 420 200, 560 250 C 700 300, 900 240, 1088 150 L1088 250 C 900 330, 700 360, 540 330 C 380 300, 250 280, 114 285 Z" fill="url(#swooshShade)"/>
      <path class="swoosh-glow" d="M114 70 L1088 70 L1088 90 C 800 90, 500 100, 114 150 Z" fill="var(--body-light)" opacity="0.25"/>
      <path class="purple-wave" d="M114 312 C 300 322, 460 342, 600 350 C 780 358, 940 320, 1088 290 L1088 318 C 940 350, 780 384, 600 378 C 440 372, 300 345, 114 340 Z" fill="var(--purple)"/>
      <path class="purple-wave-light" d="M114 334 C 300 340, 460 360, 600 372 C 780 380, 940 350, 1088 318 L1088 326 C 940 360, 780 390, 600 386 C 460 380, 300 356, 114 350 Z" fill="var(--purple-light)" opacity="0.6"/>
      <rect class="base-band" x="114" y="400" width="974" height="20" fill="var(--purple)"/>
      <rect class="base-edge" x="114" y="420" width="974" height="10" fill="var(--body-light)"/>
    </g>

    <!-- ribbon -->
    <g class="ribbon">
      <polygon points="484,98 498,104 498,140 484,148 490,124" fill="var(--purple)"/>
      <polygon points="674,86 660,94 660,132 674,136 668,112" fill="var(--purple)"/>
      <polygon points="496,100 662,90 662,134 496,144" fill="var(--white)" stroke="var(--purple)" stroke-width="3"/>
    </g>

    <!-- small icon area -->
    <rect class="bite-icon" x="354" y="136" width="60" height="46" rx="20" fill="var(--cream)" role="img" aria-label="Small bite icon"/>

    <!-- product photo area -->
    <path class="wafer-photo" d="M792 300 L950 188 L1000 200 L1060 300 L1070 360 L1030 390 L940 370 L850 410 L800 380 Z" fill="url(#waferShade)" role="img" aria-label="Photo of chocolate wafer fingers"/>
  </svg>

  <div class="brand-badge">Dorvenn</div>
  <div class="flavour-ribbon">New flavour</div>
  <h1 class="product-name">Mokarund</h1>
  <p class="tagline">Take your bite</p>
</div>
</body>
</html>
```